Gourmet food company looking for a dazzling label for their premuim vinagrette dressings

Need a food label that will dazzle our customer and prove what a premium product we have. We make high end gourmet dressing for vegetables, fruit, meat, poultry and fish.

Our label will fit on a 250 mil Tolvenka Square bottle. Labels should be a 4x5 or even 5x5 depending on the design. Nutritionals, bar codes and company blurb will be supplied later. We really want to test you all's talent on this one and are very excited to see your renderings!

Our dressings are Champagne Pear Vinaigrette, White Balsmic Vinaigrette, Mojito Lime Vinaigrette, Creamy-Avacado Lime Vinaigrette, and Asian Sesame Vinaigrette. I hope these names will help you envision our product and kinda what we are looking for.
Updates

Thank you all so far for your renderings.I really don't want pictures if that helps. Our logo can be smaller and/or the name of the product bigger. Perhaps we can even redesign Velora and remove the leaf as I don't really care for what I see yet.So good luck and thanks Added Friday, August 19, 2016

I am still looking for that clean - elegant design for our product as our product is just that. If you look on the internet at vinegars and oils you will see many designs that are simple yet elegant. Creative lettering, bordering, color (can be black and white) and size will help accomplish this. So I invite you to use all your creativity and help me find just what we need.Many thanks Added Tuesday, August 23, 2016

Project Deadline Extended Reason: So many great designs coming in that I wanted a few extra days to tweek!Great job all Added Friday, August 26, 2016

Project Deadline Extended Reason: Very good designs thus far. We just need a few more days.Thanks Added Wednesday, August 31, 2016

Target Market(s)

High end grocery and specialty stores.

Our side panel on the label will say "At Velora we're fanatics for great flavors and are passionate about finding the best ingredients. From simple to elegant our products are "simply velora".

Industry/Entity Type

It Company

Font styles to use
Serif
Decorative
Script

Requirements
Must have
• A label that will draw the consumer to pick it up! Need something bold and elegant...
Nice to have
• Again, I really would like to have a label that pops. Since the bottle front is only about 2inches in width it will need some creativity. Would like something very simple and elegant.
• If the designer does not like the logo, please feel free to design without it!
Should not have
• Dark dark colors. We are selling dressing and we don't want any colors that may distort the contents.
• No stock photos for the front. I don't want our dressing to look like the others on the self. Brambleth Kitchen just uses lettering and a their packaging is eye catching

```html
<!DOCTYPE html>
<html lang="en">
<head>
<meta charset="utf-8">
<title>Velora Vinaigrette Labels</title>
<link rel="stylesheet" href="https://fonts.googleapis.com/css2?family=Pinyon+Script&family=Playfair+Display:wght@700&family=Cormorant+Garamond:ital,wght@0,500;1,500&display=swap">
<style>
  :root {
    --backdrop: #eeeeee;
    --label-white: #ffffff;
    --panel-cream: #f3f0dc;
    --panel-blush: #ebe5e1;
    --panel-blush-light: #f4f1ef;
    --olive: #8a9463;
    --olive-deep: #5b4c1d;
    --ink: #2e2a22;
  }
  * { margin: 0; padding: 0; box-sizing: border-box; }
  html, body {
    width: 1200px; height: 853px; overflow: hidden;
    background: var(--backdrop);
  }
  .stage { position: relative; width: 1200px; height: 853px; }
  .label {
    position: absolute; top: 210px;
    width: 434px; height: 432px;
    background: var(--label-white);
    box-shadow: 8px 10px 14px rgba(0,0,0,0.28);
  }
  .label--balsamic { left: 111px; }
  .label--pear { left: 650px; }
  .label__panel {
    position: absolute; left: 10px; top: 10px;
    width: 413px; height: 312px;
  }
  .label--balsamic .label__panel { background: var(--panel-cream); }
  .label--pear .label__panel {
    background: radial-gradient(ellipse at center, var(--panel-blush-light) 0%, var(--panel-blush) 100%);
  }
  .brand, .flavour, .product-type, .volume {
    position: absolute; left: 0; width: 100%; text-align: center;
    white-space: nowrap;
  }
  .brand {
    top: 97px;
    font-family: "Cormorant Garamond", serif;
    font-weight: 500; font-size: 14px;
    letter-spacing: 0.32em; color: var(--ink);
  }
  .flavour {
    top: 172px;
    font-family: "Pinyon Script", cursive;
    font-size: 46px; line-height: 60px;
    color: var(--olive);
  }
  .product-type {
    top: 221px;
    font-family: "Playfair Display", serif;
    font-weight: 700; font-size: 32px; line-height: 40px;
    letter-spacing: 0.03em; color: var(--olive-deep);
  }
  .volume {
    top: 362px;
    font-family: "Cormorant Garamond", serif;
    color: var(--olive);
  }
  .volume__amount { font-size: 22px; font-weight: 500; font-variant-numeric: oldstyle-nums; }
  .volume__unit { font-size: 17px; font-style: italic; margin-left: 4px; }
</style>
</head>
<body>
<main class="stage">
  <section class="label label--balsamic">
    <div class="label__panel">
      <p class="brand">VELORA</p>
      <h2 class="flavour">White Balsmic</h2>
      <p class="product-type">VINAIGRETTE</p>
    </div>
    <p class="volume"><span class="volume__amount">250</span><span class="volume__unit">mil</span></p>
  </section>

  <section class="label label--pear">
    <div class="label__panel">
      <p class="brand">VELORA</p>
      <h2 class="flavour">Champagne Pear</h2>
      <p class="product-type">VINAIGRETTE</p>
    </div>
    <p class="volume"><span class="volume__amount">250</span><span class="volume__unit">mil</span></p>
  </section>
</main>
</body>
</html>
```